business card for a shoe shop

we would like a business card for a family owned shoe shop.
With this information included.
Darnell's Shoe Store
Family owned since 1947

then on other side
Darnell's Shoe Store
Footwear fitting specialist
Phone: 9187 2630
218 Quarry St, Fernleigh Downs 3187
(cnr. Hartwick Rd and Quarry St)
darnellshoes218@examplemail.com
if could incorporate the purple color on card i have attached.

```html
<!DOCTYPE html>
<html lang="en">
<head>
<meta charset="utf-8">
<title>Darnell's Shoe Store – Business Card</title>
<link rel="stylesheet" href="https://fonts.googleapis.com/css2?family=Anton&family=Archivo:wght@600&family=Roboto:wght@400;700;900&display=swap">
<style>
  :root {
    --page: #ffffff;
    --brand-blue: #235a78;
    --pattern-navy: #133f5d;
    --accent-purple: #5b3b8c;
    --ink: #111111;
    --white: #ffffff;
  }
  html, body {
    margin: 0;
    padding: 0;
    width: 900px;
    height: 1200px;
    overflow: hidden;
    background: var(--page);
  }
  .canvas {
    position: relative;
    width: 900px;
    height: 1200px;
  }
  .card {
    position: absolute;
    left: 110px;
    width: 688px;
    height: 393px;
    background: var(--brand-blue);
    box-shadow: 0 2px 14px rgba(0, 0, 0, 0.35);
    overflow: hidden;
  }
  .card--front { top: 128px; }
  .card--back { top: 612px; }
  .pattern-panel {
    position: absolute;
    background: var(--pattern-navy);
  }
  .card--front .pattern-panel--left { left: 0; top: 91px; width: 128px; height: 214px; }
  .card--front .pattern-panel--right { right: 0; top: 98px; width: 123px; height: 214px; }
  .card--back .pattern-panel--left { left: 0; top: 91px; width: 49px; height: 214px; }

  .brand {
    position: absolute;
    text-align: center;
    color: var(--white);
    white-space: nowrap;
  }
  .brand__name {
    margin: 0;
    font-family: "Anton", "Arial Narrow", sans-serif;
    font-weight: 400;
    line-height: 1;
    text-transform: uppercase;
  }
  .brand__tagline {
    margin: 0;
    font-family: "Archivo", Arial, sans-serif;
    font-weight: 600;
    text-transform: uppercase;
    line-height: 1;
  }
  .card--front .brand { left: 143px; top: 104px; width: 400px; }
  .card--front .brand__name { font-size: 72px; letter-spacing: 4px; }
  .card--front .brand__name + .brand__name { margin-top: 11px; }
  .card--front .brand__tagline { font-size: 19px; letter-spacing: 2.2px; margin-top: 12px; }

  .contact-side {
    position: absolute;
    top: 0;
    right: 0;
    width: 279px;
    height: 100%;
    background: var(--white);
  }
  .card--back .brand { left: 58px; top: 132px; width: 300px; }
  .card--back .brand__name { font-size: 52px; letter-spacing: 3px; }
  .card--back .brand__name + .brand__name { margin-top: 8px; }
  .card--back .brand__tagline { font-size: 12.5px; letter-spacing: 1.2px; margin-top: 7px; }

  .contact-icon {
    position: absolute;
    left: 385px;
    width: 48px;
    height: 48px;
  }
  .contact-icon--phone { top: 84px; }
  .contact-icon--email { top: 157px; }
  .contact-icon--address { top: 231px; }

  .contact-text {
    position: absolute;
    left: 442px;
    margin: 0;
    font-family: "Roboto", Arial, sans-serif;
    color: var(--ink);
    white-space: nowrap;
  }
  .contact-text--phone { top: 91px; font-size: 29px; font-weight: 900; letter-spacing: 0.5px; }
  .contact-text--email { top: 175px; font-size: 13.5px; }
  .contact-text--address { top: 238px; font-size: 13.5px; line-height: 18px; }
</style>
</head>
<body>
<div class="canvas">

  <section class="card card--front">
    <div class="pattern-panel pattern-panel--left" role="img" aria-label="Dark navy geometric cube pattern panel"></div>
    <div class="pattern-panel pattern-panel--right" role="img" aria-label="Dark navy geometric cube pattern panel"></div>
    <div class="brand">
      <p class="brand__name">Darnell's</p>
      <p class="brand__name">Shoe Store</p>
      <p class="brand__tagline">Family Owned Since 1947</p>
    </div>
  </section>

  <section class="card card--back">
    <div class="pattern-panel pattern-panel--left" role="img" aria-label="Dark navy geometric cube pattern panel"></div>
    <div class="brand">
      <p class="brand__name">Darnell's</p>
      <p class="brand__name">Shoe Store</p>
      <p class="brand__tagline">Footwear Fitting Specialist</p>
    </div>

    <div class="contact-side"></div>

    <svg class="contact-icon contact-icon--phone" viewBox="0 0 48 48" aria-hidden="true">
      <circle cx="24" cy="24" r="23" fill="var(--white)"/>
      <circle cx="24" cy="24" r="20" fill="var(--accent-purple)"/>
      <path d="M17.5 13.5c1-.6 2.1-.3 2.7.6l2 3.2c.5.9.3 2-.5 2.6l-1.4 1c.9 2.3 2.6 4.1 4.9 5l1-1.4c.6-.8 1.8-1 2.6-.4l3.2 2c.9.6 1.2 1.800.6 2.7l-1 1.6c-.8 1.3-2.4 1.9-3.9 1.4-6-2-10.2-6.3-12.2-12.2-.5-1.5.1-3.1 1.4-3.900z" fill="var(--white)"/>
    </svg>
    <p class="contact-text contact-text--phone">9187 2630</p>

    <svg class="contact-icon contact-icon--email" viewBox="0 0 48 48" aria-hidden="true">
      <circle cx="24" cy="24" r="23" fill="var(--white)"/>
      <circle cx="24" cy="24" r="20" fill="var(--accent-purple)"/>
      <rect x="13" y="16" width="22" height="16" rx="1.5" fill="none" stroke="var(--white)" stroke-width="2.4"/>
      <path d="M15.5 18.5 24 26l8.5-7.5" fill="none" stroke="var(--white)" stroke-width="2.4" stroke-linejoin="round"/>
    </svg>
    <p class="contact-text contact-text--email">darnellshoes218@examplemail.com</p>

    <svg class="contact-icon contact-icon--address" viewBox="0 0 48 48" aria-hidden="true">
      <circle cx="24" cy="24" r="23" fill="var(--white)"/>
      <circle cx="24" cy="24" r="20" fill="var(--accent-purple)"/>
      <path d="M24 11.5c-4.9 0-8.5 3.7-8.5 8.4 0 6 8.5 16.6 8.5 16.6s8.5-10.6 8.5-16.6c0-4.7-3.6-8.4-8.5-8.4z" fill="var(--white)"/>
      <circle cx="24" cy="20" r="3.2" fill="var(--accent-purple)"/>
    </svg>
    <p class="contact-text contact-text--address">218 Quarry St, Fernleigh Downs 3187<br>(cnr. Hartwick Rd and Quarry St)</p>
  </section>

</div>
</body>
</html>
```